Thoroughbred Racing Partnership needs web design

Crown of Laurels Partners is a management group who buys horses and races them on both the West and East coasts. The premise of the business is for an investment as little as $500, anyone can be a partner and own a percentage of a horse(s). This is a low cost way of getting involved in the exciting sport of Thoroughbred Racing, without shouldering the heavy financial responsibility. Our target market is mostly males 40+ but we want to include all target markets. We are looking for something very clean and professional, we want to give an image of success. Nothing overly "artsy." I have included the logo in which you can incorporate in the site. Also, the logo colors will be the colors of our "silks." The silks are what the jockey wears and will be an important marketing tool for COL. We would like a very prominent picture of a racehorse somewhere on the homepage, we want to make it clear that is a website for Horseracing partnerships.

On the top of the site, it should say "Crown of Laurels" (on the top)
and below that "Thoroughbred Racing Partnerships." (below that)

The main sections, which should be across the top are:

Home
About Us
Ownership
Stable Roster
News
Contact us

Some of these will have drop down menus.

An example of a competitor website that we like is: www.harrowfieldstable.example
An example of a competitor website that we don't like is: www.gallopmarket.example
Updates

Project Deadline Extended
Reason: We have a Board of Directors meeting on the 22nd and we will be making a decision on that day. I'm giving an extension so that all designers are able to submit their designs by the 22nd. Thank you!

Target Market(s)

40+ males

Industry/Entity Type

Business

Requirements
Must have
• our logo must be on the site. We would like at least one bold image of a thoroughbred horse in action. The picture is going to tell the story so it needs to be very eye-catching.

Our slogan should also be included on the website, "Experience the thrill of owning a Racehorse."
Should not have
• cartoons, artsy pictures, pictures of Steeplechase horses or "jumpers." This partnership is for racehorses only, there is not jumping involved with the horses.

```html
<!DOCTYPE html>
<html lang="en">
<head>
<meta charset="utf-8">
<title>Crown of Laurels – Thoroughbred Racing Partnerships</title>
<link href="https://fonts.googleapis.com/css2?family=Arvo:ital,wght@0,400;0,700;1,400&family=Source+Sans+3:wght@300;400;600&family=Open+Sans:wght@400;600&display=swap" rel="stylesheet">
<style>
:root{
  --gold:#d89c16;
  --gold-light:#e6ae2a;
  --bg:#1c1c1c;
  --bg-deep:#141414;
  --panel:#2b2b2b;
  --panel-dark:#161616;
  --text:#ffffff;
  --muted:#bdbdbd;
  --line:#3b3b3b;
}
*{margin:0;padding:0;box-sizing:border-box}
html,body{width:1200px;height:2347px;overflow:hidden}
body{position:relative;background:var(--bg);color:var(--text);font-family:"Source Sans 3",Arial,sans-serif}
.abs{position:absolute}
.backdrop{left:0;top:155px;width:1200px;height:1823px;background:radial-gradient(ellipse at 50% 15%,#4a4a4a 0%,#2a2a2a 35%,#1a1a1a 70%),#1c1c1c}
.topbar{left:0;top:0;width:1200px;height:40px;background:#111;font:11px "Open Sans",sans-serif;color:#9a9a9a}
.topbar .contact{left:17px;top:12px}
.social{display:flex;gap:8px}
.social span{width:15px;height:15px;background:#9a9a9a;display:block}
.topbar .social{right:17px;top:12px;position:absolute}
.header{left:0;top:40px;width:1200px;height:115px;background:#1a1a1a}
.brand{left:44px;top:28px;font-family:"Arvo",serif;font-weight:700;color:#fff;text-align:center;line-height:1}
.brand .mark{font-size:40px;letter-spacing:3px}
.brand .sub{font-size:15px;letter-spacing:3px;margin-top:4px}
.site-title{right:32px;top:26px;text-align:right}
.site-title h1{font:italic 400 40px "Arvo",serif;letter-spacing:1px}
.site-title p{font:300 22px "Source Sans 3",sans-serif;color:var(--gold);margin-top:2px}
.nav{left:0;top:155px;width:1200px;height:52px;background:#1e1e1e;display:flex;padding-left:17px}
.nav a{color:#fff;text-decoration:none;font:600 16px "Open Sans",sans-serif;height:52px;line-height:52px;padding:0 20px;letter-spacing:.5px}
.nav a.active{background:var(--gold)}
.nav a.open{background:var(--gold);margin-left:6px}
.dropdown{left:362px;top:207px;width:164px;height:185px;background:#262626;border-left:4px solid var(--gold)}
.dropdown li{list-style:none;font:600 11px "Open Sans",sans-serif;color:#ddd;height:34px;line-height:34px;padding-left:12px}
.dropdown li:first-child{margin-top:14px}
.slider{left:146px;top:207px;width:908px;height:356px;background:linear-gradient(90deg,#6a4a35 0%,#9a7050 30%,#8b6a55 55%,#b8a08a 100%)}
.slide-title{left:632px;top:232px;width:379px;height:56px;background:var(--gold);font:700 33px "Source Sans 3",sans-serif;text-align:center;line-height:56px}
.slide-sub{left:632px;top:295px;width:379px;height:44px;background:rgba(30,30,30,.85);font:300 32px "Source Sans 3",sans-serif;text-align:center;line-height:44px}
.slide-arrow{width:34px;height:34px;border-radius:50%;background:#111;top:367px}
.slogan{left:0;top:588px;width:1200px;text-align:center;font:700 37px "Arvo",serif;letter-spacing:2px}
.lead{left:0;top:650px;width:1200px;text-align:center;font:300 32px/42px "Source Sans 3",sans-serif;color:#cfcfcf;letter-spacing:1px}
.lead em{font-style:normal;color:var(--gold)}
.btn-hero{left:449px;top:748px;width:289px;height:50px;background:var(--gold);font:300 31px "Source Sans 3",sans-serif;line-height:50px;padding-left:80px}
.btn-hero svg{position:absolute;left:22px;top:15px}
.features{left:8px;top:860px;width:1184px;height:199px;background:var(--panel);display:flex}
.feature{position:relative;width:296px;padding:22px 0 0 10px}
.feature.events{background:var(--panel-dark);width:292px;margin:6px 0;padding-top:16px;border:1px solid #333}
.feature h3{font:700 27px "Arvo",serif;display:flex;align-items:center;gap:14px}
.feature p{font:12px/19px "Open Sans",sans-serif;color:#ddd;margin-top:14px;width:270px}
.btn-sm{display:flex;align-items:center;gap:12px;width:122px;height:38px;background:#0d0d0d;font:13px "Open Sans",sans-serif;padding-left:12px;margin-top:16px}
.btn-sm.gold{background:var(--gold)}
.video{left:46px;top:1089px;width:416px;height:202px;background:#1a1a1a}
.video .frame{position:absolute;left:0;top:0;width:416px;height:182px;background:linear-gradient(180deg,#8aa07a 0%,#6e8f3c 55%,#5f8a2e 100%)}
.video .play{position:absolute;left:172px;top:55px;width:72px;height:50px;border-radius:8px;background:rgba(0,0,0,.75)}
.video .bar{position:absolute;left:0;top:182px;width:416px;height:20px;background:#222;font:10px "Open Sans",sans-serif;color:#ccc}
.about{left:617px;top:1128px;width:560px}
.about h2{font:700 26px "Arvo",serif}
.about p{font:13px/19px "Open Sans",sans-serif;color:#e6e6e6;margin-top:10px}
.btn-md{left:981px;top:1234px;width:172px;height:40px;background:var(--gold);font:17px "Source Sans 3",sans-serif;display:flex;align-items:center;gap:14px;padding-left:12px}
.horses-title{left:17px;top:1362px;font:700 27px "Arvo",serif;color:var(--gold)}
.horses-lead{left:17px;top:1403px;font:13px "Open Sans",sans-serif;color:#eee}
.pager{left:17px;top:1436px;width:57px;height:20px;background:var(--gold);display:flex;justify-content:space-around;align-items:center}
.tile{top:1458px;height:202px;border:1px solid #3a3a3a}
.tile-overlay{left:18px;top:1458px;width:285px;height:202px;background:rgba(25,25,25,.55);text-align:center}
.tile-overlay h4{font:700 22px "Arvo",serif;margin-top:22px;letter-spacing:1px}
.tile-overlay p{font:13px "Open Sans",sans-serif;color:#ccc;margin-top:4px}
.tile-overlay .icon{position:absolute;left:131px;top:133px;width:32px;height:26px;background:var(--gold)}
.testimonial{left:17px;top:1726px;width:1158px;height:197px;background:#222;border-top:2px solid #555}
.testimonial h2{position:absolute;left:18px;top:26px;font:700 29px "Arvo",serif;letter-spacing:1px}
.testimonial .who{position:absolute;left:18px;top:68px;font:300 30px "Source Sans 3",sans-serif;color:var(--gold)}
.testimonial .who span{font-size:20px;color:#fff;font-weight:400}
.testimonial p{position:absolute;left:18px;top:108px;width:1000px;font:15px/26px "Source Sans 3",sans-serif;color:#bbb}
.btn-outline{left:909px;top:1872px;width:244px;height:36px;background:#111;border:1px solid #555;font:300 20px "Source Sans 3",sans-serif;display:flex;align-items:center;gap:8px;padding-left:12px}
.footer{left:0;top:1978px;width:1200px;height:319px;background:#262626}
.footer h5{position:absolute;top:38px;font:400 18px "Arvo",serif;color:#ddd;letter-spacing:.5px}
.tweet{position:absolute;left:17px;font:12px/25px "Open Sans",sans-serif;color:#ddd}
.tweet a{color:var(--gold);text-decoration:none}
.tweet small{color:#999;font-size:11px}
.thumb{position:absolute;width:42px;height:33px;border:1px solid #555;background:linear-gradient(135deg,#6b5a4a,#2f2925)}
.touch{position:absolute;left:617px;top:99px;font:12px/22px "Open Sans",sans-serif;color:#ccc}
.touch .mail{color:var(--gold)}
.phone{position:absolute;left:617px;top:170px;display:flex;align-items:center;gap:12px;font:600 30px "Source Sans 3",sans-serif;color:var(--gold)}
.footer .social{position:absolute;left:617px;top:242px;gap:12px}
.footer .social span{width:14px;height:14px;background:#aaa}
.field{position:absolute;background:#f2f2f2;font:11px "Open Sans",sans-serif;color:#888}
.submit{position:absolute;left:1071px;top:240px;width:106px;height:38px;background:var(--gold);font:15px "Source Sans 3",sans-serif;display:flex;align-items:center;gap:14px;padding-left:12px}
.bottombar{left:0;top:2297px;width:1200px;height:50px;background:#1a1a1a;border-top:1px solid var(--line);font:12px "Open Sans",sans-serif;color:#aaa}
.bottombar .copy{position:absolute;left:17px;top:18px}
.bottombar nav{position:absolute;right:60px;top:18px;color:#ddd;word-spacing:2px}
.to-top{position:absolute;right:8px;top:8px;width:36px;height:34px;background:#444}
</style>
</head>
<body>
<div class="abs backdrop" role="img" aria-label="Dark blurred racetrack scene behind the page"></div>

<div class="abs topbar">
  <div class="abs contact">● 18 Paddock Row , UK &nbsp; ▯ 1.555.010.2040</div>
  <div class="social"><span></span><span></span><span></span><span></span></div>
</div>

<header class="abs header">
  <div class="abs brand"><div class="mark">COL</div><div class="sub">PARTNERS</div></div>
  <div class="abs site-title">
    <h1>Crown of Laurels</h1>
    <p>Thoroughbred Racing Partnerships</p>
  </div>
</header>

<nav class="abs nav">
  <a class="active">Home</a><a>About Us</a><a>Ownership</a><a class="open">Stable Roster ↓</a><a>News</a><a>Contact</a>
</nav>

<div class="abs slider" role="img" aria-label="Jockey in orange silks riding a racehorse at full gallop"></div>
<div class="abs slide-title">Lorem ipsum dolor</div>
<div class="abs slide-sub">Sed ut perspiciatis</div>
<div class="abs slide-arrow" style="left:148px"><svg width="34" height="34"><path d="M19 11l-6 6 6 6" stroke="#fff" stroke-width="2.5" fill="none"/></svg></div>
<div class="abs slide-arrow" style="left:1014px"><svg width="34" height="34"><path d="M15 11l6 6-6 6" stroke="#fff" stroke-width="2.5" fill="none"/></svg></div>

<ul class="abs dropdown">
  <li>Stable Roster 1</li><li>Stable Roster 1</li><li>Stable Roster 1</li><li>Stable Roster 1</li><li>Stable Roster 1</li>
</ul>

<h2 class="abs slogan">Experience the thrill of owning a Racehorse</h2>
<p class="abs lead">Be a part of the thrilling event with just an<br>investment of as little as <em>$500</em></p>
<div class="abs btn-hero"><svg width="30" height="20"><path d="M2 10h22M16 3l8 7-8 7M6 4v12" stroke="#fff" stroke-width="3" fill="none"/></svg>Know How</div>

<section class="abs features">
  <div class="feature">
    <h3><svg width="26" height="26"><circle cx="13" cy="8" r="6" fill="#d89c16"/><path d="M1 26c0-8 5-11 12-11s12 3 12 11z" fill="#d89c16"/></svg>Ownership</h3>
    <p>Lorem ipsum dolor sit amet, consectetur adipisicing elit, sed do eiusmod tempor incididunt ut labore</p>
    <div class="btn-sm gold"><svg width="12" height="12"><path d="M1 6h9M6 2l4 4-4 4" stroke="#fff" stroke-width="2" fill="none"/></svg>Read More</div>
  </div>
  <div class="feature">
    <h3><svg width="28" height="26"><path d="M1 12L27 1 18 25 13 15z" fill="#d89c16"/></svg>Stable Roster</h3>
    <p>Lorem ipsum dolor sit amet, consectetur adipisicing elit, sed do eiusmod tempor incididunt ut labore</p>
    <div class="btn-sm"><svg width="12" height="12"><path d="M1 6h9M6 2l4 4-4 4" stroke="#fff" stroke-width="2" fill="none"/></svg>Read More</div>
  </div>
  <div class="feature">
    <h3><svg width="24" height="30"><path d="M0 0h17l7 7v23H0z" fill="#d89c16"/><path d="M5 12h14M5 17h14M5 22h14" stroke="#2b2b2b" stroke-width="2"/></svg>News</h3>
    <p>Lorem ipsum dolor sit amet, consectetur adipisicing elit, sed do eiusmod tempor incididunt ut labore</p>
    <div class="btn-sm"><svg width="12" height="12"><path d="M1 6h9M6 2l4 4-4 4" stroke="#fff" stroke-width="2" fill="none"/></svg>Read More</div>
  </div>
  <div class="feature events">
    <h3><svg width="28" height="28"><rect x="2" y="4" width="24" height="22" rx="2" stroke="#d89c16" stroke-width="3" fill="none"/><path d="M2 10h24M8 1v6M20 1v6" stroke="#d89c16" stroke-width="3"/></svg>Events</h3>
    <p>Lorem ipsum dolor sit amet, consectetur adipisicing elit, sed do eiusmod tempor incididunt ut labore</p>
    <div class="btn-sm"><svg width="12" height="12"><path d="M1 6h9M6 2l4 4-4 4" stroke="#fff" stroke-width="2" fill="none"/></svg>Read More</div>
  </div>
</section>

<div class="abs video">
  <div class="frame" role="img" aria-label="Video still of racehorses galloping on a green turf course"></div>
  <div class="play"><svg width="72" height="50"><path d="M29 14l18 11-18 11z" fill="#fff"/></svg></div>
  <div class="bar"><svg width="416" height="20"><path d="M8 5l8 5-8 5z" fill="#ccc"/><rect x="36" y="9" width="210" height="2" fill="#555"/><rect x="36" y="9" width="40" height="2" fill="#c22"/><circle cx="76" cy="10" r="4" fill="#ddd"/><text x="100" y="14" fill="#ccc" font-size="9" font-family="Open Sans">0:02 / 4:17</text><rect x="396" y="5" width="10" height="10" fill="none" stroke="#ccc"/></svg></div>
</div>
<div class="abs about">
  <h2>About Us</h2>
  <p>Lorem ipsum dolor sit amet, consectetur adipisicing elit, sed do eiusmod tempor incididunt ut labore et dolore magna aliqua. Ut enim ad minim veniam, quis nostrud exercitation ullamco laboris nisi ut aliquip ex ea commodo consequat.</p>
</div>
<div class="abs btn-md"><svg width="14" height="14"><path d="M1 7h11M7 2l5 5-5 5" stroke="#fff" stroke-width="2.5" fill="none"/></svg>Read More</div>

<h2 class="abs horses-title">The Horses of Choice</h2>
<p class="abs horses-lead">Lorem ipsum dolor sit amet, consectetur adipisicing elit, sed do eiusmod tempor incididunt ut</p>
<div class="abs pager"><svg width="14" height="10"><path d="M13 5H2M6 1L2 5l4 4" stroke="#fff" stroke-width="1.6" fill="none"/></svg><svg width="14" height="10"><path d="M1 5h11M8 1l4 4-4 4" stroke="#fff" stroke-width="1.6" fill="none"/></svg></div>
<div class="abs tile" style="left:18px;width:285px;background:linear-gradient(135deg,#6a3a22,#2d1d15)" role="img" aria-label="Close view of a bay horse's neck"></div>
<div class="abs tile" style="left:313px;width:284px;background:linear-gradient(135deg,#8a8070,#3a2a20)" role="img" aria-label="Dark horse wearing a race saddle cloth"></div>
<div class="abs tile" style="left:602px;width:285px;background:linear-gradient(135deg,#6a3028,#b08878)" role="img" aria-label="Racehorse in a red hood and blinkers"></div>
<div class="abs tile" style="left:894px;width:284px;background:linear-gradient(135deg,#4a3a20,#d8c8a0)" role="img" aria-label="Pale horse with flowing mane"></div>
<div class="abs tile-overlay"><h4>Lorem Ipsum</h4><p>Sed ut perspiciatis unde omnis</p><div class="icon"><svg width="32" height="26"><rect x="9" y="7" width="14" height="12" fill="none" stroke="#fff" stroke-width="1.6"/><path d="M10 18l5-5 3 3 2-2 3 4" stroke="#fff" fill="none"/></svg></div></div>

<section class="abs testimonial">
  <h2>See what our&nbsp; Partners are saying</h2>
  <div class="who">Alan Mercer, <span>CEO. Brightfurlong Ltd.</span></div>
  <p>Lorem ipsum dolor sit amet, consectetur adipisicing elit, sed do eiusmod tempor incididunt ut labore et dolore magna aliqua. Ut enim ad minim veniam, quis nostrud exercitation ullamco laboris nisi ut aliquip ex ea commodo consequat.</p>
</section>
<div class="abs btn-outline"><svg width="28" height="22"><path d="M2 11h22M15 3l9 8-9 8" stroke="#fff" stroke-width="2.5" fill="none"/></svg>View All Testimonials</div>

<footer class="abs footer">
  <h5 style="left:17px">Latest Tweets</h5>
  <h5 style="left:314px">Latest Album</h5>
  <h5 style="left:617px">Get In Touch</h5>
  <h5 style="left:907px">Quick Contact</h5>

  <div class="tweet" style="top:88px">▸ Lorem ipsum dolor sit ---- I am Owen<br><a>http://video.example/k7Rm2xQ</a> <small>2013/10/24</small></div>
  <div class="tweet" style="top:148px">▸ Lorem ipsum dolor sit ---- I am Owen<br><a>http://video.example/k7Rm2xQ</a> <small>2013/10/24</small></div>
  <div class="tweet" style="top:209px">▸ Lorem ipsum dolor sit ---- I am Owen<br><a>http://video.example/k7Rm2xQ</a> <small>2013/10/24</small></div>
  <div class="tweet" style="top:269px">▸ Lorem ipsum dolor sit ---- I am Owen<br><a>http://video.example/k7Rm2xQ</a> <small>2013/10/24</small></div>

  <div role="img" aria-label="Grid of racing photo thumbnails">
    <div class="thumb" style="left:314px;top:87px"></div><div class="thumb" style="left:372px;top:87px"></div><div class="thumb" style="left:430px;top:87px"></div><div class="thumb" style="left:488px;top:87px"></div>
    <div class="thumb" style="left:314px;top:135px"></div><div class="thumb" style="left:372px;top:135px"></div><div class="thumb" style="left:430px;top:135px"></div><div class="thumb" style="left:488px;top:135px"></div>
    <div class="thumb" style="left:314px;top:183px"></div><div class="thumb" style="left:372px;top:183px"></div><div class="thumb" style="left:430px;top:183px"></div><div class="thumb" style="left:488px;top:183px"></div>
  </div>

  <div class="touch">72 Fenwick Meadow Lane<br>Greyridge, KY 40999<br><span class="mail">✉ hello@crownoflaurels.example</span></div>
  <div class="phone"><svg width="22" height="40"><rect x="1" y="1" width="20" height="38" rx="4" fill="none" stroke="#aaa" stroke-width="2"/><rect x="4" y="6" width="14" height="24" fill="#aaa"/></svg>155501020400</div>
  <div class="social"><span></span><span></span><span></span><span></span></div>

  <div class="field" style="left:909px;top:94px;width:121px;height:27px;text-align:center;line-height:27px">Name</div>
  <div class="field" style="left:1056px;top:94px;width:121px;height:27px;text-align:center;line-height:27px">Email</div>
  <div class="field" style="left:909px;top:131px;width:268px;height:101px;padding:6px 10px">Message</div>
  <div class="submit"><svg width="14" height="14"><path d="M1 7h11M7 2l5 5-5 5" stroke="#fff" stroke-width="2.5" fill="none"/></svg>Submit</div>
</footer>

<div class="abs bottombar">
  <div class="copy">@Copyright message</div>
  <nav>Home About Us Ownership Stable Roster News Contact</nav>
  <div class="to-top"><svg width="36" height="34"><path d="M11 20l7-7 7 7" stroke="#ccc" stroke-width="2.5" fill="none"/></svg></div>
</div>
</body>
</html>
```